Business Card Design

We are a business based in Sydney repairing and restoring timber windows. We mainly cater to residential home owners although sometimes work with larger building companies. We do a lot of work in heritage buildings though also cater to modern windows.
Our Logo is Black and Gold and were thinking of using a white card with only these two colours although we are open to any design suggestions. Check out our website for ideas.
Front of Card
Contact Information, Website & Business Name
Back of Card
Business Logo, website?
Target Market(s)
Home Owners
Industry/Entity Type
Residential
Contact Information for Business Card
Oakridge Sash Revivals
Marcus Pellow
0472 309 648
marcus@oakridgesashrevivals.example
www.oakridgesashrevivals.example
Look and feel

```html
<!DOCTYPE html>
<html lang="en">
<head>
<meta charset="utf-8">
<title>Oakridge Sash Revivals – Business Card</title>
<link href="https://fonts.googleapis.com/css2?family=Open+Sans:wght@400;600&display=swap" rel="stylesheet">
<style>
  :root {
    --canvas: #efefed;
    --card-white: #f7f7f6;
    --card-grey: #e4e4e2;
    --frame: #fafafa;
    --ink: #3b3a37;
    --gold: #8a7436;
    --panel-text: #eeeeea;
    --photo-light: #d9d4c9;
    --photo-mid: #b9ae98;
    --photo-warm: #c9a66a;
    --photo-dark: #6e665a;
  }
  * { box-sizing: border-box; margin: 0; padding: 0; }
  html, body { width: 1200px; height: 900px; overflow: hidden; }
  body {
    background: var(--canvas);
    font-family: "Open Sans", Arial, sans-serif;
    position: relative;
  }
  .card {
    position: absolute;
    left: 320px;
    width: 560px;
    height: 320px;
    box-shadow: 0 6px 18px rgba(0,0,0,0.12);
    overflow: hidden;
  }

  /* ---------- Back of card ---------- */
  .card-back { top: 100px; background: var(--frame); }
  .back-scene {
    position: absolute; inset: 16px;
    background:
      linear-gradient(90deg, rgba(255,255,255,0.55) 0%, rgba(255,255,255,0) 30%),
      linear-gradient(180deg, var(--photo-light) 0%, var(--photo-warm) 38%, var(--photo-mid) 60%, var(--photo-dark) 100%);
    box-shadow: inset 0 0 0 2px #dcdcda;
  }
  .back-logo {
    position: absolute; left: 50%; top: 30px; transform: translateX(-50%);
    width: 128px; height: 128px; border-radius: 50%;
    background: var(--card-white);
    display: flex; align-items: center; justify-content: center; text-align: center;
  }
  .logo-name {
    font-weight: 600; color: var(--ink);
    font-size: 15px; line-height: 1.25;
  }
  .back-web {
    position: absolute; left: 50%; top: 172px; transform: translateX(-50%);
    background: var(--ink); color: var(--panel-text);
    font-size: 10px; padding: 2px 10px; white-space: nowrap;
  }
  .back-contact {
    position: absolute; left: 50%; top: 200px; transform: translateX(-50%);
    background: var(--ink); color: var(--panel-text);
    font-size: 13px; line-height: 1.4; text-align: center;
    padding: 10px 16px; white-space: nowrap;
  }

  /* ---------- Front of card ---------- */
  .card-front {
    top: 480px;
    background: linear-gradient(180deg, var(--card-white) 0%, var(--card-grey) 100%);
  }
  .front-logo {
    position: absolute; left: 48px; top: 34px;
    width: 132px; height: 132px; border-radius: 50%;
    background: var(--card-white);
    box-shadow: 0 0 0 1px #cfcfcc;
    display: flex; align-items: center; justify-content: center; text-align: center;
  }
  .front-web {
    position: absolute; left: 38px; top: 178px;
    background: var(--ink); color: var(--panel-text);
    font-size: 10px; padding: 2px 8px; white-space: nowrap;
  }
  .front-contact {
    position: absolute; left: 22px; top: 206px;
    background: var(--ink); color: var(--panel-text);
    border: 3px solid var(--gold);
    font-size: 12px; line-height: 1.45; padding: 8px 12px;
    white-space: nowrap;
  }
  .front-contact .rule { border-top: 1px solid #8a8984; margin: 4px 0; }
  .front-window { position: absolute; left: 306px; top: 20px; width: 232px; height: 232px; }
</style>
</head>
<body>

  <section class="card card-back" aria-label="Back of business card">
    <div class="back-scene" role="img" aria-label="Soft blurred photo of a bright home interior"></div>
    <div class="back-logo"><span class="logo-name">Oakridge<br>Sash Revivals</span></div>
    <div class="back-web">www.oakridgesashrevivals.example</div>
    <div class="back-contact">
      Oakridge Sash Revivals Marcus Pellow 0472 309 648<br>
      marcus@oakridgesashrevivals.example
    </div>
  </section>

  <section class="card card-front" aria-label="Front of business card">
    <div class="front-logo"><span class="logo-name">Oakridge<br>Sash Revivals</span></div>
    <div class="front-web">www.oakridgesashrevivals.example</div>
    <div class="front-contact">
      Oakridge Sash Revivals<br>
      Marcus Pellow 0472 309 648
      <div class="rule"></div>
      marcus@oakridgesashrevivals.example
    </div>
    <svg class="front-window" viewBox="0 0 236 236">
      <defs>
        <linearGradient id="pane-view" x1="0" y1="0" x2="0" y2="1">
          <stop offset="0" stop-color="#e6e1d6"/>
          <stop offset="0.4" stop-color="#cdb98f"/>
          <stop offset="1" stop-color="#7b7262"/>
        </linearGradient>
      </defs>
      <rect x="0" y="0" width="236" height="236" fill="#fafafa" stroke="#d2d2cf"/>
      <rect x="14" y="14" width="208" height="208" fill="url(#pane-view)" role="img" aria-label="Photo of a dining room seen through the window panes"/>
      <rect x="111" y="14" width="14" height="208" fill="#fafafa"/>
      <rect x="14" y="111" width="208" height="14" fill="#fafafa"/>
      <rect x="14" y="14" width="208" height="208" fill="none" stroke="#d2d2cf"/>
    </svg>
  </section>

</body>
</html>
```